Tri-fold Brochure Design for Banking Business

The brochure we have needs to be improved - more business like and more attractive. Logo file and brochure is attached. I would like to be able to edit the text after you get done. Your ideas and changes to text are welcome. See our website www.quillbrookadvisory.com for our theme. We can use indesign to edit the text after you complete. However, please make changes to the text we have in the design that it uploaded. Your comments and changes are welcome.

Target Market(s)

Human Resources and learning & development staff at the global investment banks - Fenwright Carrow, QTRV, etc.

Industry/Entity Type

Investment Banking

Logo Text

Quillbrook Advisory Group

Font styles to use
Serif
Sans Serif

Colors
33a6d7
0493ce
3277b5
fbf289
fdf9cf
fbee3e
0555a3
85acd3

Requirements
Must have
• Must be similar to our website www.quillbrookadvisory.com. Needs to be business-like, clean fonts, sharp design. Our logo - of course.
Nice to have
• City images - seems to be our theme.

```html
<!DOCTYPE html>
<html lang="en">
<head>
<meta charset="utf-8">
<title>Quillbrook Advisory Group – Tri-fold Brochure</title>
<link href="https://fonts.googleapis.com/css2?family=Montserrat:wght@600;700;800&family=Open+Sans:wght@400;600;700&display=swap" rel="stylesheet">
<style>
:root{
  --blue:#0555a3;
  --blue-mid:#3277b5;
  --blue-light:#85acd3;
  --yellow:#fbee3e;
  --yellow-deep:#e8d21e;
  --cream:#fdf9cf;
  --white:#ffffff;
  --ink:#4a4a4a;
  --page:#ebe9ea;
}
*{margin:0;padding:0;box-sizing:border-box}
html,body{width:880px;height:1200px;overflow:hidden;background:var(--page)}
body{position:relative;font-family:"Open Sans",Arial,sans-serif;color:var(--ink)}
.spread{position:absolute;left:40px;width:800px;height:568px;background:var(--white);overflow:hidden;box-shadow:0 2px 6px rgba(0,0,0,.25)}
.spread--outside{top:21px}
.spread--inside{top:611px}
.spread-art{position:absolute;inset:0;width:800px;height:568px}
.block{position:absolute}
.tag{position:absolute;left:0;height:24px;padding:0 26px 0 18px;background:var(--yellow);color:var(--blue);font:700 12px "Montserrat",Arial,sans-serif;line-height:24px;text-transform:uppercase;clip-path:polygon(0 0,100% 0,85% 100%,0 100%)}
.copy{font-size:8.6px;line-height:1.3;text-align:justify}
.copy p{margin-bottom:9px}
.copy--light{color:var(--white)}
.copy--dark{color:#5b5b5b}
.contact-head{position:absolute;left:293px;top:12px;width:214px;text-align:center;font:700 11.5px "Montserrat",Arial,sans-serif;color:var(--blue);text-transform:uppercase}
.contact{position:absolute;left:308px;width:184px;height:32px;border:1px solid var(--white);display:flex;flex-direction:column;align-items:center;justify-content:center;gap:2px;text-align:center}
.contact b{display:block;font:800 8px/1.1 "Montserrat",Arial,sans-serif;color:var(--blue);text-transform:uppercase}
.contact span{display:block;font-size:7.2px;line-height:1.1;color:var(--blue)}
.caption{position:absolute;left:267px;width:266px;text-align:center;font:700 8.6px "Open Sans",Arial,sans-serif;color:#333}
.url{font:700 8.5px "Montserrat",Arial,sans-serif;letter-spacing:.08em}
.brand{position:absolute;left:548px;width:236px;top:336px;display:flex;align-items:center;justify-content:center;gap:8px}
.brand-mark{width:14px;height:14px;background:var(--blue)}
.brand-name{font:700 15px "Montserrat",Arial,sans-serif;color:var(--blue)}
.tagline{position:absolute;left:533px;width:267px;top:370px;text-align:center;font:700 15px/1.35 "Montserrat",Arial,sans-serif;color:#222;text-transform:uppercase}
.benefits{list-style:none;font-size:8.6px;color:var(--white)}
.benefits li{margin-bottom:7px}
.benefits li::before{content:"»";color:var(--yellow);font-weight:700;margin-right:5px;font-size:11px}
.section-title{position:absolute;font:700 12px "Montserrat",Arial,sans-serif;color:var(--blue);text-transform:uppercase}
.cta{position:absolute;left:557px;top:142px;width:219px;height:46px;background:var(--yellow);display:flex;align-items:center;justify-content:center;text-align:center;font:800 11px/1.25 "Montserrat",Arial,sans-serif;color:var(--blue);text-transform:uppercase}
</style>
</head>
<body>

<section class="spread spread--outside">
  <svg class="spread-art" viewBox="0 0 800 568" xmlns="http://www.w3.org/2000/svg">
    <defs>
      <linearGradient id="cityDusk" x1="0" y1="0" x2="0" y2="1">
        <stop offset="0" stop-color="#a9c4dd"/><stop offset=".55" stop-color="#6b7f93"/><stop offset="1" stop-color="#2e3b4a"/>
      </linearGradient>
      <linearGradient id="citySkyline" x1="0" y1="0" x2="0" y2="1">
        <stop offset="0" stop-color="#cfe0ee"/><stop offset=".6" stop-color="#8a8f95"/><stop offset="1" stop-color="#4c5560"/>
      </linearGradient>
      <linearGradient id="mapTone" x1="0" y1="0" x2="1" y2="1">
        <stop offset="0" stop-color="#6e6e6e"/><stop offset="1" stop-color="#9a9a9a"/>
      </linearGradient>
    </defs>
    <polygon points="0,0 533,0 533,240 267,330 0,250" fill="var(--blue)"/>
    <polygon points="0,262 267,342 267,568 0,568" fill="url(#cityDusk)" role="img" aria-label="Photo of a glass skyscraper and modern riverside offices"/>
    <polygon points="0,250 267,330 267,342 0,262" fill="var(--yellow)"/>
    <polygon points="267,330 533,240 533,252 267,342" fill="var(--yellow)"/>
    <polygon points="533,0 800,0 800,255 700,305 533,235" fill="url(#citySkyline)" role="img" aria-label="Photo of a city skyline across the water"/>
    <polyline points="533,242 700,313 800,263" fill="none" stroke="var(--yellow)" stroke-width="9"/>
    <polyline points="533,250 700,321 800,271" fill="none" stroke="var(--blue)" stroke-width="3"/>
    <polygon points="293,0 507,0 507,245 400,275 293,245" fill="var(--yellow-deep)"/>
    <rect x="308" y="345" width="184" height="105" fill="url(#mapTone)" opacity=".8" role="img" aria-label="World map"/>
    <circle cx="400" cy="486" r="5.5" fill="none" stroke="var(--blue)" stroke-width="1.3"/>
    <ellipse cx="400" cy="486" rx="2.4" ry="5.5" fill="none" stroke="var(--blue)" stroke-width="1"/>
    <line x1="394.5" y1="486" x2="405.5" y2="486" stroke="var(--blue)" stroke-width="1"/>
    <polygon points="533,560 800,470 800,478 533,568" fill="var(--blue)"/>
    <polygon points="541,568 800,481 800,568" fill="var(--yellow)"/>
  </svg>

  <div class="tag" style="top:14px">About us</div>
  <div class="block copy copy--light" style="left:16px;top:58px;width:234px">
    <p>Quillbrook Advisory Group efficiently provides complete sales, marketing and logistical support for all our programs, no matter the location.</p>
    <p>Our globally located trainers have extensive experience, both as industry professionals and as trainers.</p>
    <p>Our highly qualified logistical team complement the training services, providing reliable and efficient support.</p>
  </div>

  <div class="contact-head">Get in touch</div>
  <div class="contact" style="top:40px"><b>Global:</b><span>nadia.verne@quillbrookadvisory.com</span></div>
  <div class="contact" style="top:86px"><b>Asia:</b><span>owen.hale@quillbrookadvisory.com</span></div>
  <div class="contact" style="top:132px"><b>United States:</b><span>lucas.brenner@quillbrookadvisory.com</span></div>
  <div class="contact" style="top:178px"><b>Europe:</b><span>clara.moss@quillbrookadvisory.com</span></div>

  <div class="caption" style="top:456px">Worldwide Training Service</div>
  <div class="caption url" style="top:500px;color:#222;font-size:7.5px">www.quillbrookadvisory.com</div>

  <div class="brand"><span class="brand-mark"></span><span class="brand-name">Quillbrook Advisory Group</span></div>
  <div class="tagline">Your expert training<br>and consulting partner</div>
  <div class="block url" style="left:618px;top:549px;color:var(--blue)">www.quillbrookadvisory.com</div>
</section>

<section class="spread spread--inside">
  <svg class="spread-art" viewBox="0 0 800 568" xmlns="http://www.w3.org/2000/svg">
    <defs>
      <linearGradient id="harbour" x1="0" y1="0" x2="0" y2="1">
        <stop offset="0" stop-color="#b9cde0"/><stop offset=".6" stop-color="#5f7d9c"/><stop offset="1" stop-color="#2b4460"/>
      </linearGradient>
      <linearGradient id="digitalBlue" x1="0" y1="0" x2="1" y2="1">
        <stop offset="0" stop-color="#33a6d7"/><stop offset=".6" stop-color="#3277b5"/><stop offset="1" stop-color="#0d3f74"/>
      </linearGradient>
      <linearGradient id="globeTeam" x1="0" y1="0" x2="0" y2="1">
        <stop offset="0" stop-color="#e3edf5"/><stop offset=".5" stop-color="#9fb6cb"/><stop offset="1" stop-color="#4f6f8d"/>
      </linearGradient>
    </defs>
    <polygon points="0,0 267,0 267,312 0,250" fill="var(--blue)"/>
    <polygon points="0,262 267,324 267,568 0,568" fill="url(#harbour)" role="img" aria-label="Photo of a harbour city skyline with a tall tower in the mist"/>
    <polygon points="0,250 267,312 267,324 0,262" fill="var(--yellow)"/>
    <polygon points="267,0 533,0 533,195 267,312" fill="url(#digitalBlue)" role="img" aria-label="Photo of a hand touching a digital screen showing training, mentor, motivation and skill keywords"/>
    <polygon points="267,0 430,0 380,52 267,52" fill="var(--yellow)"/>
    <polygon points="267,312 533,195 533,207 267,324" fill="var(--yellow)"/>
    <polygon points="533,205 800,205 800,378 533,480" fill="url(#globeTeam)" role="img" aria-label="Photo of business people standing on top of a globe"/>
    <polygon points="660,205 800,205 800,232" fill="var(--yellow)"/>
    <polygon points="533,480 800,378 800,392 533,494" fill="var(--yellow)"/>
    <polygon points="533,494 800,392 800,568 533,568" fill="var(--blue)"/>
  </svg>

  <div class="tag" style="top:14px">Why choose us?</div>
  <div class="block copy copy--light" style="left:16px;top:54px;width:234px">
    <p>Quillbrook Advisory Group is dedicated to providing you and your firm with the highest level of service.</p>
    <p>We provide dedicated sales and logistics support for each program to insure consistent, reliable results.</p>
  </div>
  <ul class="block benefits" style="left:16px;top:124px;width:240px">
    <li>Highly qualified, international pool of trainers</li>
    <li>Strong client relationship management and support</li>
    <li>Competitive pricing and flexibility</li>
    <li>Outcome driven approach directly</li>
  </ul>

  <div class="section-title" style="left:283px;top:18px;font-size:11.5px;color:#1b2b44">Why choose us?</div>
  <div class="block copy copy--dark" style="left:287px;top:345px;width:228px">
    <p>Quillbrook Advisory Group provides best in class services for all our clients.</p>
    <p>We provide highly customized programs tailored to your specific requirements.</p>
    <p>Direct interaction between our clients, consulting trainers and client service staff ensures measurable outcomes for program participants.</p>
    <p>We facilitate learning outcomes using a blended methodology combining interactive analysis, hands-on experiential models, market simulations and a state-of-the-art learning management system.</p>
    <p>Our material databanks are continuously updated to insure accuracy and effectiveness of our services.</p>
  </div>

  <div class="section-title" style="left:551px;top:18px">Our team</div>
  <div class="block copy copy--dark" style="left:551px;top:44px;width:230px">
    <p>Our Consulting Trainers are located globally and recognized by the industry as highly effective trainers and program facilitators.</p>
    <p>Quillbrook provides global expertise for our programs with local talent for program facilitation.</p>
  </div>
  <div class="cta">Need more information?<br>Contact us!</div>
  <div class="block url" style="left:553px;top:532px;color:var(--white);font-size:7.6px;letter-spacing:.02em">www.quillbrookadvisory.com</div>
</section>

</body>
</html>
```